Monthly Mailed Newsletter/Magazine for Medical Spa

Every month we send out a mailed newsletter/magazine to our visitors from the previous month. We made a sample newsletter/magazine as a guideline of what we are looking for. We need a designer to make a simple and clean design layout.

- Attached is our sample design that has all the content we want to use.
- Newsletter/magazine is 8 pages total.
- Size of each page is 8.5 inches in width by 11 inches in height.
- Content and images can be located here: https://files.example-vault.net/folders/8kqTRuW2nBv5xhZ0pLm4YdC7sEa1Gf9Jo?view=open

The following will give you an idea of our brand presentation.
Our website is: www.LumaDermGlow.com
Our Instagram; @lumadermglow
Our Facebook: www.friendspace.example/lumadermglow

Target Market(s)

Women 25 - 45

Industry/Entity Type

Beauty

Font styles to use
Other font styles liked:
• Josefins Sans Bold & Lato

Colors
f78f20
ffffff

Requirements
Must have
• - Our Logo
- Our tagline: YOUR SKIN DESERVES IT!
- Address and contact information for our locations
- Our color scheme: Black and #FAA641
- Heading font is Josefin Sans Bold
- Paragraph font is Lato
- Our website address: www.LumaDermGlow.com

```html
<!DOCTYPE html>
<html lang="en">
<head>
<meta charset="utf-8">
<title>Luma Derm Glow Newsletter – Spread</title>
<link href="https://fonts.googleapis.com/css2?family=Josefin+Sans:wght@400;600;700&family=Lato:wght@400;700&display=swap" rel="stylesheet">
<style>
  :root {
    --orange: #f2a040;
    --orange-light: #efb366;
    --orange-deep: #ea9432;
    --ink: #1c1c1c;
    --paper: #ffffff;
    --backdrop: #e6dcd6;
    --photo-warm: #e9ddd5;
    --photo-cool: #dfe3e8;
    --photo-pink: #eedbe4;
  }
  * { box-sizing: border-box; margin: 0; padding: 0; }
  html, body {
    width: 1200px; height: 824px; overflow: hidden;
    background: var(--backdrop);
  }
  .spread {
    position: absolute; left: 20px; top: 37px;
    width: 1160px; height: 750px;
    display: flex;
    box-shadow: 0 6px 24px rgba(80, 60, 50, 0.18);
  }
  .page { position: relative; width: 580px; height: 750px; overflow: hidden; }

  /* Back cover */
  .back-cover {
    background: linear-gradient(160deg, var(--orange-light) 0%, var(--orange) 55%, var(--orange-deep) 100%);
    color: var(--paper);
  }
  .cover-tagline {
    position: absolute; left: 0; right: 0; top: 300px;
    text-align: center;
    font-family: "Josefin Sans", sans-serif; font-weight: 600;
    letter-spacing: 3px; line-height: 1.1;
  }
  .cover-tagline .line-one { font-size: 30px; }
  .cover-tagline .line-one strong { font-size: 44px; font-weight: 700; }
  .cover-tagline .line-two { font-size: 32px; display: block; }
  .locations {
    position: absolute; left: 60px; right: 40px; bottom: 60px;
    font-family: "Josefin Sans", sans-serif; font-size: 11px; line-height: 1.55;
    display: flex; justify-content: space-between; align-items: flex-end;
  }
  .locations h3 { font-size: 14px; font-weight: 600; letter-spacing: 1px; margin-bottom: 8px; }
  .location { padding-left: 8px; }

  /* Inside page */
  .inside-page { background: var(--paper); color: var(--ink); }
  .brand {
    position: absolute; left: 0; right: 0; top: 34px;
    text-align: center;
  }
  .brand-name {
    font-family: "Josefin Sans", sans-serif; font-weight: 700;
    font-size: 28px; color: var(--ink);
  }
  .article-title {
    position: absolute; left: 40px; top: 112px; width: 260px;
    font-family: "Josefin Sans", sans-serif; font-weight: 700;
    font-size: 19px; line-height: 1.2;
  }
  .intro {
    position: absolute; left: 50px; top: 166px; width: 270px;
    font-family: "Lato", sans-serif; font-size: 11px; line-height: 1.35;
  }
  .photo { position: absolute; }
  .photo-facial { left: 340px; top: 92px; width: 210px; height: 140px; background: linear-gradient(135deg, var(--photo-cool), var(--photo-warm)); }
  .photo-leg { left: 60px; top: 272px; width: 270px; height: 150px; background: linear-gradient(135deg, var(--photo-cool), #f1ece9); }
  .photo-underarm { left: 345px; top: 250px; width: 215px; height: 140px; background: linear-gradient(135deg, var(--photo-pink), #f4eaef); }
  .body-copy {
    position: absolute; left: 70px; top: 440px; width: 290px;
    font-family: "Josefin Sans", sans-serif; font-size: 13.5px; line-height: 1.35;
  }
  .callout {
    position: absolute; left: 380px; top: 405px; width: 190px; height: 230px;
    background: var(--orange); color: var(--paper);
    padding: 24px 16px;
    font-family: "Josefin Sans", sans-serif; font-size: 13.5px; line-height: 1.4;
  }
  .footer-band {
    position: absolute; left: 0; right: 0; bottom: 34px; height: 26px;
    background: var(--orange); color: var(--paper);
    display: flex; justify-content: space-between; align-items: center;
    padding: 0 18px;
    font-family: "Josefin Sans", sans-serif; font-weight: 600;
  }
  .footer-band .site { font-size: 12px; }
  .footer-band .tagline { font-size: 13px; font-weight: 700; letter-spacing: 0.5px; }
</style>
</head>
<body>
<main class="spread">
  <section class="page back-cover">
    <h2 class="cover-tagline">
      <span class="line-one">YOUR <strong>SKIN</strong></span>
      <span class="line-two">DESERVES IT!</span>
    </h2>
    <div class="locations">
      <div>
        <h3>Locations</h3>
        <p class="location">Tucson<br>318 East Saguaro Lane, Suite 210<br>Tucson, AZ 85716<br>Call/Text: 520-555-0148<br>Email: hello@lumadermglow.com</p>
      </div>
      <div>
        <p class="location">Yuma, AZ<br>1470 West Palm Street, Suite B<br>Yuma, AZ 85365<br>Call/Text: 928-555-0193<br>Email: hello@lumadermglow.com</p>
      </div>
    </div>
  </section>

  <section class="page inside-page">
    <div class="brand">
      <span class="brand-name">Luma Derm Glow</span>
    </div>

    <h1 class="article-title">Is At-home Laser Hair Removal Effective?</h1>
    <p class="intro">“I love how prickly your skin feels,” said no one ever! Did you know that the average modern woman shaves 7,718 times in one lifetime? That’s a whole lot of bristling, ingrown hairs, and skin irritation. Thankfully laser treatments have rendered razors obsolete.</p>

    <div class="photo photo-facial" role="img" aria-label="Photo of a client receiving a laser facial treatment"></div>
    <div class="photo photo-underarm" role="img" aria-label="Photo of underarm laser hair removal with a handheld device"></div>
    <div class="photo photo-leg" role="img" aria-label="Photo of a client on a treatment chair receiving leg laser hair removal"></div>

    <p class="body-copy">If you’re already a firm laser believer, the marketability of handy at-home DIY products can be appealing. But many are left perplexed at their effectiveness.<br>Here are some unbiased professional opinions to zap away your FAQs.<br>How does laser hair removal work?</p>

    <aside class="callout">Laser hair removal uses a concentrated beam of light to target melanin, also known as your natural pigment. Through this, the follicle that produces hair is damaged. This delays the future growth of hairs.</aside>

    <footer class="footer-band">
      <span class="site">www.LumaDermGlow.com</span>
      <span class="tagline">YOUR SKIN DESERVES IT!</span>
    </footer>
  </section>
</main>
</body>
</html>
```